Business Cards for Financial Service Consulting Business Ltd

Business Card Design for my risk management consultancy to the financial service industry
Responsible Lending, Fair Charges, Ethical Collections

Should be serious, professional, corporate

Target Market(s)

Fintech, Financial Services Industry

Industry/Entity Type

Financial Service

Contact Information for Business Card

Marcus Pennick
marc@larchwellconsulting.co.uk
07700900418
01632960527

Font styles to use
Serif

Colors

Designer to choose colors to be used in the design.

Requirements
Must have
• Name: Larchwell Consulting
• Logo, contact details
• The three pillars of my business Responsible Lending, Fair Charges, Ethical Collections
Nice to have
• Corporate Feel
Should not have
• jokes, pretty pictures, cartoons

```html
<!DOCTYPE html>
<html lang="en">
<head>
<meta charset="utf-8">
<title>Larchwell Consulting – Business Cards</title>
<link href="https://fonts.googleapis.com/css2?family=Jost:wght@400;500;600;700&display=swap" rel="stylesheet">
<style>
  :root {
    --backdrop: #eeeeee;
    --card: #ffffff;
    --ink: #3a3a3c;
    --ink-soft: #4a4a4c;
    --on-band: #ffffff;
  }
  * { margin: 0; padding: 0; box-sizing: border-box; }
  html, body { width: 1200px; height: 1096px; overflow: hidden; }
  body {
    background: var(--backdrop);
    font-family: "Jost", "Futura", sans-serif;
    color: var(--ink);
    position: relative;
  }
  .card {
    position: absolute;
    width: 550px;
    height: 355px;
    background: var(--card);
    overflow: hidden;
  }
  .card--details { left: 491px; top: 168px; }
  .card--brand { left: 197px; top: 571px; }
  .abs { position: absolute; }

  /* Details card */
  .name-rule { left: 0; top: 69px; width: 51px; height: 3px; background: var(--ink); }
  .person-name { left: 63px; top: 36px; font-size: 27px; font-weight: 600; line-height: 1; white-space: nowrap; }
  .person-role { left: 63px; top: 65px; font-size: 18px; font-weight: 400; line-height: 1; color: var(--ink-soft); }

  .wordmark { display: flex; align-items: center; gap: 8px; }
  .wordmark__dot { border: 4px solid var(--ink); border-radius: 50%; flex: none; }
  .wordmark__text { font-weight: 600; line-height: 1; color: var(--ink); }
  .wordmark__line1 { display: block; letter-spacing: 0.5px; }
  .wordmark__line2 { display: block; }

  .card--details .wordmark { right: 8px; top: 34px; }
  .card--details .wordmark__dot { width: 38px; height: 38px; }
  .card--details .wordmark__line1 { font-size: 28px; }
  .card--details .wordmark__line2 { font-size: 17px; margin-top: 4px; padding-left: 26px; }

  .contact-icon { width: 34px; height: 34px; }
  .icon-phone { left: 19px; top: 201px; }
  .icon-mail { left: 19px; top: 243px; }
  .contact-text { left: 63px; font-size: 16px; font-weight: 600; line-height: 19px; white-space: nowrap; }
  .phones { top: 199px; }
  .email { top: 252px; }

  .bands { left: 0; top: 299px; }

  /* Brand card */
  .card--brand .email-top { right: 7px; top: 46px; font-size: 16px; font-weight: 600; white-space: nowrap; }
  .email-rule { right: 0; top: 68px; width: 133px; height: 3px; background: var(--ink); }
  .card--brand .wordmark { left: 24px; top: 196px; gap: 10px; }
  .card--brand .wordmark__dot { width: 46px; height: 46px; border-width: 5px; }
  .card--brand .wordmark__line1 { font-size: 35px; }
  .card--brand .wordmark__line2 { font-size: 21px; margin-top: 4px; padding-left: 27px; }
  .card--brand .bands { top: 299px; }
  .pillars {
    left: 11px; top: 306px;
    font-size: 16px; font-weight: 600; color: var(--on-band);
    letter-spacing: 0.3px; white-space: nowrap;
  }
</style>
</head>
<body>

<section class="card card--details" aria-label="Business card, contact side">
  <div class="abs name-rule"></div>
  <div class="abs person-name">Marcus Pennick</div>
  <div class="abs person-role">Counselor</div>

  <div class="abs wordmark">
    <span class="wordmark__dot"></span>
    <span class="wordmark__text">
      <span class="wordmark__line1">LARCHWELL</span>
      <span class="wordmark__line2">CONSULTING</span>
    </span>
  </div>

  <svg class="abs contact-icon icon-phone" viewBox="0 0 34 34" aria-hidden="true">
    <circle cx="17" cy="17" r="15.5" fill="none" stroke="var(--ink)" stroke-width="1.6"/>
    <path d="M11 10 l3 -1 l2.5 4.5 l-2 1.5 q1.5 3.5 5 5 l1.5 -2 l4.5 2.5 l-1 3 q-7 1 -12.5 -6 q-2.5 -4 -1 -7.5z" fill="none" stroke="var(--ink)" stroke-width="1.3" stroke-linejoin="round"/>
  </svg>
  <div class="abs contact-text phones">07700900418<br>01632960527</div>

  <svg class="abs contact-icon icon-mail" viewBox="0 0 34 34" aria-hidden="true">
    <circle cx="17" cy="17" r="15.5" fill="none" stroke="var(--ink)" stroke-width="1.6"/>
    <rect x="9" y="11.5" width="16" height="11" fill="none" stroke="var(--ink)" stroke-width="1.3"/>
    <path d="M9 11.5 l8 6.5 l8 -6.5 M9 22.5 l6 -5 M25 22.5 l-6 -5" fill="none" stroke="var(--ink)" stroke-width="1.3"/>
  </svg>
  <div class="abs contact-text email">marc@larchwellconsulting.co.uk</div>

  <svg class="abs bands" width="550" height="33" viewBox="0 0 550 33" aria-hidden="true">
    <polygon points="0,0 401,0 391,32 0,32" fill="var(--ink)"/>
    <polygon points="464,0 550,0 550,32 453,32" fill="var(--ink)"/>
  </svg>
</section>

<section class="card card--brand" aria-label="Business card, brand side">
  <div class="abs email-top">marc@larchwellconsulting.co.uk</div>
  <div class="abs email-rule"></div>

  <div class="abs wordmark">
    <span class="wordmark__dot"></span>
    <span class="wordmark__text">
      <span class="wordmark__line1">LARCHWELL</span>
      <span class="wordmark__line2">CONSULTING</span>
    </span>
  </div>

  <svg class="abs bands" width="550" height="33" viewBox="0 0 550 33" aria-hidden="true">
    <polygon points="0,0 401,0 391,32 0,32" fill="var(--ink)"/>
    <polygon points="464,0 550,0 550,32 453,32" fill="var(--ink)"/>
  </svg>
  <div class="abs pillars">Lending - Fair Charges - Ethical Collections</div>
</section>

</body>
</html>
```